Business Card Design Project

I am a property development company requiring a professional looking business card.
The name of the my company is PLW CANOPIES. I have attached a couple of designs that I have created on my own, that can give you an idea of what I am after.
Above the wording PLW CANOPIES, I have a orange arc above these words to signify the sun is begining to rise above the horizon.
I have a few designs; Middle Rays, Side Rays, Horizontals Rays which are OK, but I am looking for the better design.
The Rear design of the card is what I had came up with. If you have a better design, I am happy to see it.
The design of the card can follow what I have came up with, or it can be totally different. The fonts needs to be adjusted to another font that is more suitable.
The colours that I have used is what I think I would like to stick with. As I have mentioned, the orange arc is to signify the sun rising. If you have a better colour scheme, I would consider it.
Looking at dealing with first home buyers and proffesional people.
Business

```html
<!DOCTYPE html>
<html lang="en">
<head>
<meta charset="utf-8">
<title>PLW Canopies – Business Card Concepts</title>
<link rel="stylesheet" href="https://fonts.googleapis.com/css2?family=Source+Sans+3:wght@400;600&display=swap">
<style>
  :root {
    --backdrop: #d9dadb;
    --card: #ffffff;
    --ink: #231f20;
    --tone-cream: #f9f3c6;
    --tone-light: #fbb570;
    --tone-mid: #f7892f;
    --tone-deep: #f8680c;
    --tone-blue: #1ba3dd;
    --tone-magenta: #e2097a;
    --tone-orange: #ef7d0d;
    --tone-yellow: #fccb00;
    --tone-green: #b3c800;
  }
  html, body { margin: 0; padding: 0; overflow: hidden; }
  body { width: 1200px; height: 1145px; background: var(--backdrop); }
  .sheet { display: block; width: 1200px; height: 1145px; }
  .card-face { fill: var(--card); }
  .brand { font-family: "Source Sans 3", sans-serif; font-weight: 600; font-size: 18px; fill: var(--ink); }
  .tagline { font-family: "Source Sans 3", sans-serif; font-size: 7.6px; fill: var(--ink); }
  .person { font-family: "Source Sans 3", sans-serif; font-size: 13.5px; fill: var(--ink); }
  .role { font-family: "Source Sans 3", sans-serif; font-size: 11.5px; fill: var(--ink); }
  .contact { font-family: "Source Sans 3", sans-serif; font-size: 9.6px; fill: var(--ink); }
  .centered { text-anchor: middle; }
  .stop-cream { stop-color: var(--tone-cream); }
  .stop-light { stop-color: var(--tone-light); }
  .stop-mid { stop-color: var(--tone-mid); }
  .stop-deep { stop-color: var(--tone-deep); }
  .stop-blue { stop-color: var(--tone-blue); }
  .stop-magenta { stop-color: var(--tone-magenta); }
  .stop-orange { stop-color: var(--tone-orange); }
  .stop-yellow { stop-color: var(--tone-yellow); }
  .stop-green { stop-color: var(--tone-green); }
</style>
</head>
<body>
<svg class="sheet" viewBox="0 0 846 807" xmlns="http://www.w3.org/2000/svg" role="img" aria-label="Six business card layouts for PLW Canopies">
  <defs>
    <clipPath id="rounded-card"><rect width="354" height="216" rx="24"/></clipPath>
    <linearGradient id="warm-down" x1="0" y1="0" x2="0" y2="1">
      <stop offset="0" class="stop-cream"/><stop offset="0.4" class="stop-light"/>
      <stop offset="0.7" class="stop-mid"/><stop offset="1" class="stop-deep"/>
    </linearGradient>
    <linearGradient id="warm-up" x1="0" y1="1" x2="0" y2="0">
      <stop offset="0" class="stop-cream"/><stop offset="0.4" class="stop-light"/>
      <stop offset="0.7" class="stop-mid"/><stop offset="1" class="stop-deep"/>
    </linearGradient>
    <linearGradient id="spectrum" x1="0" y1="0" x2="0" y2="1">
      <stop offset="0" class="stop-blue"/><stop offset="0.25" class="stop-magenta"/>
      <stop offset="0.5" class="stop-orange"/><stop offset="0.75" class="stop-yellow"/>
      <stop offset="1" class="stop-green"/>
    </linearGradient>
  </defs>

  <!-- Side rays, rounded -->
  <g class="card side-rays-rounded" transform="translate(60 58)">
    <g clip-path="url(#rounded-card)">
      <rect class="card-face" width="354" height="216"/>
      <rect class="sun-rays" x="240" y="0" width="114" height="216" fill="url(#warm-down)" role="img" aria-label="Fanned sun-ray graphic in cream and orange"/>
    </g>
    <text class="brand" x="18" y="57">PLW CANOPIES</text>
    <text class="tagline" x="44" y="70">Property Developments</text>
    <text class="person" x="40" y="105">Marcus Lowe</text>
    <text class="role" x="40" y="123">Director</text>
    <text class="contact" x="40" y="151">0400 318 552</text>
    <text class="contact" x="40" y="164">marcus@plwcanopies.com.au</text>
    <text class="contact" x="40" y="177">www.plwcanopies.com.au</text>
    <text class="contact" x="40" y="190">27 Kellet Street Kirrawee NSW 2232 Australia</text>
  </g>

  <!-- Side rays, square -->
  <g class="card side-rays-square" transform="translate(433 58)">
    <rect class="card-face" width="354" height="216"/>
    <rect class="sun-rays" x="240" y="10" width="104" height="196" fill="url(#warm-down)" role="img" aria-label="Fanned sun-ray graphic in cream and orange"/>
    <text class="brand" x="18" y="57">PLW CANOPIES</text>
    <text class="tagline" x="44" y="70">Property Developments</text>
    <text class="person" x="41" y="105">Marcus Lowe</text>
    <text class="role" x="41" y="123">Director</text>
    <text class="contact" x="41" y="151">0400 318 552</text>
    <text class="contact" x="41" y="164">marcus@plwcanopies.com.au</text>
    <text class="contact" x="41" y="177">www.plwcanopies.com.au</text>
    <text class="contact" x="41" y="190">27 Kellet Street Kirrawee NSW 2232 Australia</text>
  </g>

  <!-- Middle rays, rounded -->
  <g class="card middle-rays-rounded" transform="translate(60 295)">
    <g clip-path="url(#rounded-card)">
      <rect class="card-face" width="354" height="216"/>
      <rect class="sun-rays" x="200" y="0" width="154" height="216" fill="url(#warm-up)" role="img" aria-label="Fanned sun-ray graphic in orange and cream"/>
    </g>
    <text class="brand centered" x="99" y="52">PLW CANOPIES</text>
    <text class="tagline" x="46" y="64">Property Developments</text>
    <text class="person centered" x="99" y="104">Marcus Lowe</text>
    <text class="role centered" x="99" y="122">Director</text>
    <text class="contact centered" x="99" y="142">27 Kellet Street Kirrawee</text>
    <text class="contact centered" x="99" y="155">NSW 2232 Australia</text>
    <text class="contact centered" x="99" y="168">0400 318 552</text>
    <text class="contact centered" x="99" y="181">marcus@plwcanopies.com.au</text>
    <text class="contact centered" x="99" y="194">www.plwcanopies.com.au</text>
  </g>

  <!-- Middle rays, square -->
  <g class="card middle-rays-square" transform="translate(433 295)">
    <rect class="card-face" width="354" height="216"/>
    <rect class="sun-rays" x="240" y="10" width="104" height="196" fill="url(#warm-up)" role="img" aria-label="Fanned sun-ray graphic in orange and cream"/>
    <text class="brand" x="18" y="58">PLW CANOPIES</text>
    <text class="tagline" x="44" y="70">Property Developments</text>
    <text class="person" x="41" y="105">Marcus Lowe</text>
    <text class="role" x="41" y="123">Director</text>
    <text class="contact" x="41" y="150">0400 318 552</text>
    <text class="contact" x="41" y="163">marcus@plwcanopies.com.au</text>
    <text class="contact" x="41" y="176">www.plwcanopies.com.au</text>
    <text class="contact" x="41" y="189">27 Kellet Street Kirrawee NSW 2232 Australia</text>
  </g>

  <!-- Horizontal rays, rounded -->
  <g class="card horizontal-rays-rounded" transform="translate(60 531)">
    <g clip-path="url(#rounded-card)">
      <rect class="card-face" width="354" height="216"/>
      <rect class="sun-rays" x="200" y="0" width="154" height="216" fill="url(#warm-down)" role="img" aria-label="Fanned sun-ray graphic in cream and orange"/>
    </g>
    <text class="brand centered" x="99" y="53">PLW CANOPIES</text>
    <text class="tagline" x="46" y="65">Property Developments</text>
    <text class="person centered" x="99" y="105">Marcus Lowe</text>
    <text class="role centered" x="99" y="123">Director</text>
    <text class="contact centered" x="99" y="143">27 Kellet Street Kirrawee</text>
    <text class="contact centered" x="99" y="156">NSW 2232 Australia</text>
    <text class="contact centered" x="99" y="169">0400 318 552</text>
    <text class="contact centered" x="99" y="182">marcus@plwcanopies.com.au</text>
    <text class="contact centered" x="99" y="195">www.plwcanopies.com.au</text>
  </g>

  <!-- Multicolour rays, square -->
  <g class="card spectrum-rays-square" transform="translate(433 531)">
    <rect class="card-face" width="354" height="216"/>
    <rect class="sun-rays" x="240" y="10" width="104" height="196" fill="url(#spectrum)" role="img" aria-label="Fanned multicolour ray graphic"/>
    <text class="brand" x="18" y="58">PLW CANOPIES</text>
    <text class="tagline" x="44" y="70">Property Developments</text>
    <text class="person" x="41" y="105">Marcus Lowe</text>
    <text class="role" x="41" y="123">Director</text>
    <text class="contact" x="41" y="151">0400 318 552</text>
    <text class="contact" x="41" y="164">marcus@plwcanopies.com.au</text>
    <text class="contact" x="41" y="177">www.plwcanopies.com.au</text>
    <text class="contact" x="41" y="190">27 Kellet Street Kirrawee NSW 2232 Australia</text>
  </g>
</svg>
</body>
</html>
```